Need new Spot UV Business Card design

We are looking for a new business card design incorporating Spot UV in black & white options / versions. See examples files and Mireno Castel Design logo.
You can see our website at www.mirenocastel-example.ca. We want something classy but yet modern. We are open to black or black and/or white on white with the spot uv. We are open to portrait or landscape. Size should be standard 3.5" x 2". The front of the card should focus on the logo and name "Mireno Castel" only. Fonts used should be "Open sans" or "PT Sans".

Target Market(s)

Mid to high end

Industry/Entity Type

Business

Contact Information for Business Card

Tobin Ferrash
555.304.8172
tobin@mirenocastel-example.ca
www.mirenocastel-example.ca
4917 Alderwick Blvd. W Suite 308
Mississauga, ON K7R 2B9

Requirements
Must have
• Name & Logo

```html
<!DOCTYPE html>
<html lang="en">
<head>
<meta charset="utf-8">
<title>Mireno Castel Design – Spot UV Business Card</title>
<link rel="stylesheet" href="https://fonts.googleapis.com/css2?family=Open+Sans:wght@300;400&family=Roboto:wght@300&display=swap">
<style>
  :root {
    --sheet-bg: #e6e6e6;
    --title-ink: #6b6b6b;
    --card-black: #1b1b1b;
    --card-black-edge: #161616;
    --card-white: #ffffff;
    --logo-shadow-ink: #0c0c0c;
    --uv-white: #f4f4f4;
    --uv-muted: #9a9a9a;
    --print-ink: #1a1a1a;
    --print-muted: #555555;
    --showcase-bg: #1c1e1e;
    --showcase-ink: #55595a;
  }
  html, body {
    margin: 0;
    padding: 0;
  }
  body {
    width: 1200px;
    height: 2862px;
    overflow: hidden;
    background: var(--sheet-bg);
    position: relative;
    font-family: "Open Sans", sans-serif;
  }
  .section-title {
    position: absolute;
    left: 141px;
    margin: 0;
    font-family: "Roboto", sans-serif;
    font-weight: 300;
    font-size: 42px;
    line-height: 1;
    color: var(--title-ink);
  }
  .card {
    position: absolute;
    left: 141px;
    width: 948px;
    height: 540px;
    overflow: hidden;
  }
  .card--black {
    background: radial-gradient(ellipse at 50% 40%, var(--card-black) 0%, var(--card-black-edge) 100%);
  }
  .card--white {
    left: 139px;
    background: var(--card-white);
  }
  .brand-lockup {
    position: absolute;
    display: flex;
    align-items: center;
    gap: 26px;
  }
  .brand-square {
    box-sizing: border-box;
    border: 7px solid currentColor;
    flex: none;
  }
  .brand-name {
    font-weight: 400;
    white-space: nowrap;
    line-height: 1;
  }
  .card-front .brand-lockup {
    left: 199px;
    top: 194px;
    color: var(--logo-shadow-ink);
  }
  .card-front .brand-square {
    width: 140px;
    height: 150px;
  }
  .card-front .brand-name {
    font-size: 84px;
  }
  .card-mark {
    position: absolute;
    left: 733px;
    top: 17px;
    width: 134px;
    height: 134px;
    box-sizing: border-box;
    border: 5px solid currentColor;
  }
  .contact-block {
    position: absolute;
    left: 92px;
    top: 182px;
  }
  .contact-name {
    margin: 0 0 34px;
    font-size: 31px;
    font-weight: 400;
    line-height: 1;
  }
  .contact-list {
    list-style: none;
    margin: 0;
    padding: 0;
    font-size: 28px;
    font-weight: 300;
    line-height: 41px;
  }
  .contact-list li {
    display: flex;
    align-items: flex-start;
  }
  .contact-icon {
    flex: none;
    width: 22px;
    height: 22px;
    margin: 10px 14px 0 0;
  }
  .contact-list .address-line {
    padding-left: 36px;
  }
  .card-uv {
    color: var(--uv-white);
  }
  .card-uv .contact-list {
    color: var(--uv-muted);
  }
  .card-print {
    color: var(--print-ink);
  }
  .card-print .contact-list {
    color: var(--print-muted);
  }
  .showcase {
    position: absolute;
    left: 0;
    top: 2194px;
    width: 1200px;
    height: 668px;
    background: var(--showcase-bg);
  }
  .showcase .brand-lockup {
    left: 190px;
    top: 240px;
    color: var(--showcase-ink);
  }
  .showcase .brand-square {
    width: 170px;
    height: 170px;
    border-width: 6px;
  }
  .showcase .brand-name {
    font-size: 104px;
    font-weight: 300;
  }
</style>
</head>
<body>
  <svg width="0" height="0" style="position:absolute" aria-hidden="true">
    <defs>
      <symbol id="icon-phone" viewBox="0 0 22 22">
        <circle cx="11" cy="11" r="10" fill="none" stroke="currentColor" stroke-width="1.4"/>
        <rect x="8" y="5.5" width="6" height="11" rx="1.2" fill="none" stroke="currentColor" stroke-width="1.4"/>
      </symbol>
      <symbol id="icon-mail" viewBox="0 0 22 22">
        <circle cx="11" cy="11" r="10" fill="none" stroke="currentColor" stroke-width="1.4"/>
        <rect x="6" y="7.5" width="10" height="7" fill="currentColor"/>
      </symbol>
      <symbol id="icon-web" viewBox="0 0 22 22">
        <circle cx="11" cy="11" r="10" fill="none" stroke="currentColor" stroke-width="1.4"/>
        <circle cx="11" cy="11" r="5" fill="currentColor"/>
      </symbol>
      <symbol id="icon-pin" viewBox="0 0 22 22">
        <circle cx="11" cy="11" r="10" fill="none" stroke="currentColor" stroke-width="1.4"/>
        <path d="M11 5.5a3.8 3.8 0 0 1 3.8 3.8c0 2.8-3.8 7.2-3.8 7.2s-3.8-4.4-3.8-7.2A3.8 3.8 0 0 1 11 5.5z" fill="currentColor"/>
        <circle cx="11" cy="9.3" r="1.4" fill="var(--card-white)"/>
      </symbol>
    </defs>
  </svg>

  <h2 class="section-title" style="top:88px">Business Card Front</h2>
  <section class="card card--black card-front" style="top:155px">
    <div class="brand-lockup">
      <span class="brand-square"></span>
      <span class="brand-name">Mireno Castel</span>
    </div>
  </section>

  <h2 class="section-title" style="top:784px">Business Card Front UV part</h2>
  <section class="card card--black card-uv" style="top:857px">
    <span class="card-mark"></span>
    <div class="contact-block">
      <p class="contact-name">Tobin Ferrash</p>
      <ul class="contact-list">
        <li><svg class="contact-icon"><use href="#icon-phone"/></svg>555.304.8172</li>
        <li><svg class="contact-icon"><use href="#icon-mail"/></svg>tobin@mirenocastel-example.ca</li>
        <li><svg class="contact-icon"><use href="#icon-web"/></svg>www.mirenocastel-example.ca</li>
        <li><svg class="contact-icon"><use href="#icon-pin"/></svg>4917 Alderwick Blvd. W Suite 308</li>
        <li class="address-line">Mississauga, ON K7R 2B9</li>
      </ul>
    </div>
  </section>

  <h2 class="section-title" style="top:1494px">Business Card Back</h2>
  <section class="card card--white card-print" style="top:1570px">
    <span class="card-mark" style="left:735px;top:79px"></span>
    <div class="contact-block" style="left:92px;top:186px">
      <p class="contact-name">Tobin Ferrash</p>
      <ul class="contact-list">
        <li><svg class="contact-icon"><use href="#icon-phone"/></svg>555.304.8172</li>
        <li><svg class="contact-icon"><use href="#icon-mail"/></svg>tobin@mirenocastel-example.ca</li>
        <li><svg class="contact-icon"><use href="#icon-web"/></svg>www.mirenocastel-example.ca</li>
        <li><svg class="contact-icon"><use href="#icon-pin"/></svg>4917 Alderwick Blvd. W Suite 308</li>
        <li class="address-line">Mississauga, ON K7R 2B9</li>
      </ul>
    </div>
  </section>

  <section class="showcase">
    <div class="brand-lockup">
      <span class="brand-square"></span>
      <span class="brand-name">Mireno Castel</span>
    </div>
  </section>
</body>
</html>
```